Coin collector banner ad for specialty insurance

We need a logo designed banner ad (multiple ads) to align with the coin collector market while incorporating color palette logo and call to action. Color palette of Fernholt. Dimension, images, example designs and color palette attached. The context should include 'Specialty Insurance for your coin collection' please refer to the designed examples

Target Market(s)

Coin collectors 30-65+ years of age primarily male

Industry/Entity Type

Insurance

Font styles to use
Sans Serif

Requirements
Must have
• color palette, logo, word mark, Call to Action, The words 'Specialty Insurance for your coin collection'
Nice to have
• Call to actions
Should not have
• ba

```html
<!DOCTYPE html>
<html lang="en">
<head>
<meta charset="utf-8">
<title>Fernholt Insurance – Coin Collection Banner Set</title>
<link href="https://fonts.googleapis.com/css2?family=Source+Sans+3:wght@400;600;700&display=swap" rel="stylesheet">
<style>
  :root {
    --board: #2b2b2b;
    --blue: #0f9fdc;
    --white: #ffffff;
    --ink: #1c1c1c;
    --label: #cfcfcf;
    --gold-1: #f3d58a; --gold-2: #c99a3c;
    --silver-1: #f1f1f1; --silver-2: #8f9296;
    --copper-1: #c77a56; --copper-2: #6e3520;
    --toned-1: #c9a24a; --toned-2: #5a3b6e;
  }
  * { margin: 0; padding: 0; box-sizing: border-box; }
  html, body { width: 1200px; height: 960px; overflow: hidden; background: var(--board); }
  body { position: relative; font-family: "Source Sans 3", "Source Sans Pro", Arial, sans-serif; }

  .banner { position: absolute; background: var(--blue); overflow: hidden; }
  .banner .backdrop, .banner .coins { position: absolute; left: 0; top: 0; }
  .size-label { position: absolute; color: var(--label); font-size: 16px; letter-spacing: .3px; }

  .brand { position: absolute; display: flex; align-items: center; gap: 8px; }
  .brand.stacked { flex-direction: column; gap: 10px; }
  .brand-mark { display: block; background: var(--blue); }
  .brand-name { color: var(--ink); font-weight: 600; letter-spacing: -.3px; line-height: 1; }

  .pitch { position: absolute; color: var(--white); text-align: center; display: flex; flex-direction: column; align-items: center; }
  .pitch .headline { font-weight: 700; line-height: 1.1; }
  .pitch .subline { font-weight: 400; line-height: 1.15; }
  .cta { display: inline-flex; align-items: center; justify-content: center; gap: 6px; background: var(--white); color: var(--ink); font-weight: 600; line-height: 1; }
  .cta svg { fill: var(--ink); }
</style>
</head>
<body>

<!-- 930x255 -->
<section class="banner" style="left:36px;top:36px;width:710px;height:194px">
  <svg class="backdrop" width="710" height="194"><path d="M0 0H324C400 30 410 160 340 194H0Z" fill="#fff"/></svg>
  <div class="brand stacked" style="left:20px;top:34px;width:120px">
    <span class="brand-mark" style="width:71px;height:71px"></span>
    <span class="brand-name" style="font-size:22px">FERNHOLT</span>
  </div>
  <svg class="coins" width="400" height="194" role="img" aria-label="Photograph of a silver dollar and a gold double eagle coin">
    <defs>
      <radialGradient id="g-gold" cx=".4" cy=".35"><stop offset="0" stop-color="#f3d58a"/><stop offset="1" stop-color="#b8892f"/></radialGradient>
      <radialGradient id="g-silver" cx=".4" cy=".35"><stop offset="0" stop-color="#f4f4f4"/><stop offset="1" stop-color="#85888c"/></radialGradient>
      <radialGradient id="g-copper" cx=".4" cy=".35"><stop offset="0" stop-color="#c98059"/><stop offset="1" stop-color="#5f2c18"/></radialGradient>
      <radialGradient id="g-toned" cx=".45" cy=".4"><stop offset="0" stop-color="#8a6a4a"/><stop offset=".7" stop-color="#b58a3a"/><stop offset="1" stop-color="#4b3160"/></radialGradient>
    </defs>
    <circle cx="236" cy="98" r="56" fill="url(#g-silver)"/>
    <circle cx="306" cy="98" r="76" fill="url(#g-gold)"/>
  </svg>
  <div class="pitch" style="left:420px;top:38px;width:268px">
    <span class="headline" style="font-size:27px">SPECIALTY INSURANCE</span>
    <span class="subline" style="font-size:22px">FOR YOUR COIN COLLECTION</span>
    <span class="cta" style="width:186px;height:46px;margin-top:16px;font-size:26px">Get Started <svg width="12" height="20"><path d="M0 0L12 10L0 20Z"/></svg></span>
  </div>
</section>
<div class="size-label" style="left:375px;top:248px">930X255</div>

<!-- 980x80 -->
<section class="banner" style="left:36px;top:291px;width:748px;height:60px">
  <svg class="backdrop" width="748" height="60"><path d="M0 0H400C418 15 418 45 400 60H0Z" fill="#fff"/></svg>
  <div class="brand" style="left:13px;top:12px">
    <span class="brand-mark" style="width:34px;height:34px"></span>
    <span class="brand-name" style="font-size:22px">FERNHOLT</span>
  </div>
  <svg class="coins" width="420" height="60" role="img" aria-label="Photograph of a row of seven collectible coins">
    <circle cx="212" cy="33" r="26" fill="url(#g-gold)"/>
    <circle cx="240" cy="33" r="26" fill="url(#g-silver)"/>
    <circle cx="268" cy="33" r="26" fill="url(#g-copper)"/>
    <circle cx="296" cy="33" r="26" fill="url(#g-silver)"/>
    <circle cx="324" cy="33" r="26" fill="url(#g-gold)"/>
    <circle cx="352" cy="33" r="26" fill="url(#g-silver)"/>
    <circle cx="380" cy="33" r="26" fill="url(#g-gold)"/>
  </svg>
  <div class="pitch" style="left:426px;top:12px;width:190px">
    <span class="headline" style="font-size:17px">SPECIALTY INSURANCE</span>
    <span class="subline" style="font-size:14px">FOR YOUR COIN COLLECTION</span>
  </div>
  <span class="cta" style="position:absolute;left:623px;top:18px;width:110px;height:26px;font-size:16px">Get Started <svg width="7" height="13"><path d="M0 0L7 6.5L0 13Z"/></svg></span>
</section>
<div class="size-label" style="left:376px;top:372px">980X80</div>

<!-- 980x200 -->
<section class="banner" style="left:36px;top:410px;width:748px;height:152px">
  <svg class="backdrop" width="748" height="152"><path d="M0 0H396C440 30 440 120 396 152H0Z" fill="#fff"/></svg>
  <div class="brand stacked" style="left:24px;top:30px;width:90px">
    <span class="brand-mark" style="width:52px;height:52px"></span>
    <span class="brand-name" style="font-size:18px">FERNHOLT</span>
  </div>
  <svg class="coins" width="420" height="152" role="img" aria-label="Photograph of silver, copper and gold Liberty head coins">
    <circle cx="204" cy="76" r="62" fill="url(#g-silver)"/>
    <circle cx="264" cy="76" r="64" fill="url(#g-copper)"/>
    <circle cx="336" cy="76" r="66" fill="url(#g-gold)"/>
  </svg>
  <div class="pitch" style="left:440px;top:28px;width:284px">
    <span class="headline" style="font-size:25px">SPECIALTY INSURANCE</span>
    <span class="subline" style="font-size:20px;margin-top:4px">FOR YOUR COIN COLLECTION</span>
    <span class="cta" style="width:125px;height:30px;margin-top:10px;font-size:19px">Get Started <svg width="8" height="15"><path d="M0 0L8 7.5L0 15Z"/></svg></span>
  </div>
</section>
<div class="size-label" style="left:713px;top:584px">980X200</div>

<!-- 1080x1080 -->
<section class="banner" style="left:36px;top:587px;width:360px;height:360px">
  <svg class="backdrop" width="360" height="360"><path d="M0 0H360V85C300 260 120 300 0 181Z" fill="#fff"/></svg>
  <div class="brand" style="left:14px;top:14px">
    <span class="brand-mark" style="width:39px;height:39px"></span>
    <span class="brand-name" style="font-size:27px">FERNHOLT</span>
  </div>
  <svg class="coins" width="360" height="260" role="img" aria-label="Photograph of a toned silver dollar and a copper large cent">
    <circle cx="228" cy="137" r="74" fill="url(#g-copper)"/>
    <circle cx="110" cy="165" r="82" fill="url(#g-toned)"/>
  </svg>
  <div class="pitch" style="left:0;top:262px;width:360px">
    <span class="headline" style="font-size:23px">SPECIALTY INSURANCE</span>
    <span class="subline" style="font-size:20px">FOR YOUR COIN COLLECTION</span>
    <span class="cta" style="width:117px;height:28px;margin-top:8px;font-size:17px">Get Started <svg width="7" height="14"><path d="M0 0L7 7L0 14Z"/></svg></span>
  </div>
</section>
<div class="size-label" style="left:404px;top:590px">1080X1080(BIG SIZE)</div>

<!-- 1080x1920 -->
<section class="banner" style="left:806px;top:36px;width:366px;height:650px">
  <svg class="backdrop" width="366" height="650"><path d="M0 0H366V292Q183 530 0 292Z" fill="#fff"/></svg>
  <div class="brand" style="left:55px;top:25px">
    <span class="brand-mark" style="width:48px;height:48px"></span>
    <span class="brand-name" style="font-size:30px">FERNHOLT</span>
  </div>
  <svg class="coins" width="366" height="420" role="img" aria-label="Photograph of a gold double eagle, a silver dollar and a toned silver dollar">
    <circle cx="186" cy="196" r="84" fill="url(#g-gold)"/>
    <circle cx="254" cy="308" r="68" fill="url(#g-silver)"/>
    <circle cx="130" cy="308" r="84" fill="url(#g-toned)"/>
  </svg>
  <div class="pitch" style="left:0;top:420px;width:366px">
    <span class="headline" style="font-size:36px;line-height:1.25">SPECIALTY<br>INSURANCE</span>
    <span class="subline" style="font-size:25px;margin-top:6px">FOR YOUR COIN COLLECTION</span>
    <span class="cta" style="width:167px;height:41px;margin-top:26px;font-size:24px">Get Started <svg width="10" height="19"><path d="M0 0L10 9.5L0 19Z"/></svg></span>
  </div>
</section>
<div class="size-label" style="left:1013px;top:697px">1080X1920(BIG SIZE)</div>

<!-- 1280x255 -->
<section class="banner" style="left:409px;top:742px;width:763px;height:152px">
  <svg class="backdrop" width="763" height="152"><path d="M0 0H378C430 30 430 122 378 152H0Z" fill="#fff"/></svg>
  <div class="brand stacked" style="left:16px;top:27px;width:110px">
    <span class="brand-mark" style="width:56px;height:56px"></span>
    <span class="brand-name" style="font-size:19px">FERNHOLT</span>
  </div>
  <svg class="coins" width="420" height="152" role="img" aria-label="Photograph of silver, copper and gold Liberty head coins">
    <circle cx="207" cy="78" r="62" fill="url(#g-silver)"/>
    <circle cx="267" cy="78" r="64" fill="url(#g-copper)"/>
    <circle cx="331" cy="78" r="64" fill="url(#g-gold)"/>
  </svg>
  <div class="pitch" style="left:438px;top:26px;width:306px">
    <span class="headline" style="font-size:26px">SPECIALTY INSURANCE</span>
    <span class="subline" style="font-size:22px;margin-top:4px">FOR YOUR COIN COLLECTION</span>
    <span class="cta" style="width:130px;height:30px;margin-top:8px;font-size:19px">Get Started <svg width="8" height="15"><path d="M0 0L8 7.5L0 15Z"/></svg></span>
  </div>
</section>
<div class="size-label" style="left:1022px;top:908px">1280X255(BIG SIZE)</div>

</body>
</html>
```